Business Card Design

Electronic Security
Alarm Systems
CCTV
Electronic Access Control
Security System Integration

Industry/Entity Type

Business

Contact Information for Business Card

Declan Whitfield
PO Box 862
Carrowbrook Qld 4179
Phone 07 38265014
Mob 0428615937

```html
<!DOCTYPE html>
<html lang="en">
<head>
<meta charset="utf-8">
<title>Valta Business Card</title>
<link rel="stylesheet" href="https://fonts.googleapis.com/css2?family=Mulish:wght@400;600&display=swap">
<style>
  :root {
    --page-bg: #e9e9ea;
    --card-dark: #353537;
    --card-white: #ffffff;
    --accent-blue: #23a1dc;
    --accent-orange: #f6a623;
    --text-light: #f2f2f2;
    --text-ink: #2e2e30;
  }
  html, body {
    margin: 0;
    width: 1200px;
    height: 960px;
    overflow: hidden;
    background: var(--page-bg);
    font-family: "Mulish", Arial, sans-serif;
  }
  .business-card {
    position: absolute;
    left: 150px;
    top: 205px;
    width: 900px;
    height: 550px;
    box-shadow: 0 14px 40px rgba(0,0,0,0.18);
    overflow: hidden;
  }
  .card-shapes { position: absolute; inset: 0; }
  .brand {
    position: absolute;
    left: 60px;
    top: 240px;
    display: flex;
    align-items: center;
    gap: 18px;
  }
  .brand-dot {
    width: 46px;
    height: 46px;
    border-radius: 50%;
    background: var(--accent-blue);
  }
  .brand-name {
    font-size: 64px;
    font-weight: 400;
    color: var(--text-ink);
    letter-spacing: 2px;
    line-height: 1;
  }
  .services {
    position: absolute;
    right: 44px;
    top: 62px;
    margin: 0;
    padding: 0;
    list-style: none;
    text-align: right;
    color: var(--text-light);
    font-size: 24px;
    line-height: 36px;
  }
  .services li::after {
    content: "";
    display: inline-block;
    width: 12px;
    height: 12px;
    margin-left: 16px;
    background: var(--accent-orange);
    vertical-align: 2px;
  }
  .contact {
    position: absolute;
    right: 44px;
    top: 300px;
    text-align: right;
    color: var(--text-light);
  }
  .contact-name {
    margin: 0 0 22px;
    font-size: 31px;
    font-weight: 400;
    color: var(--accent-orange);
    letter-spacing: 1px;
  }
  .contact-line {
    margin: 0;
    font-size: 24px;
    line-height: 38px;
    display: flex;
    justify-content: flex-end;
    align-items: center;
    gap: 10px;
  }
  .contact-line svg { width: 22px; height: 24px; }
  .address {
    margin-top: 28px;
    font-size: 24px;
    line-height: 36px;
  }
</style>
</head>
<body>
  <article class="business-card">
    <svg class="card-shapes" viewBox="0 0 900 550" width="900" height="550" aria-hidden="true">
      <rect width="900" height="550" fill="var(--card-dark)"/>
      <path d="M0,0 L320,0 C470,80 500,360 390,550 L0,550 Z" fill="var(--accent-orange)"/>
      <path d="M0,0 L350,0 C480,70 500,330 350,550 L0,550 Z" fill="var(--accent-blue)"/>
      <path d="M0,0 L300,0 C440,60 470,350 340,550 L0,550 Z" fill="var(--card-white)"/>
    </svg>

    <div class="brand">
      <span class="brand-dot"></span>
      <span class="brand-name">Valta</span>
    </div>

    <ul class="services">
      <li>Electronic Security</li>
      <li>Alarm Systems</li>
      <li>CCTV</li>
      <li>Electronic Access Control</li>
      <li>Security System Integration</li>
    </ul>

    <div class="contact">
      <h2 class="contact-name">DECLAN WHITFIELD</h2>
      <p class="contact-line">07 38265014
        <svg viewBox="0 0 24 24" aria-label="Phone"><path d="M6 3c-2 1-3 3-2 6 2 6 6 10 12 12 3 1 5 0 6-2l-4-4-3 2c-3-1-5-3-6-6l2-3z" fill="none" stroke="var(--accent-blue)" stroke-width="2" stroke-linejoin="round"/></svg>
      </p>
      <p class="contact-line">0428615937
        <svg viewBox="0 0 24 24" aria-label="Mobile"><rect x="6" y="2" width="12" height="20" rx="2" fill="none" stroke="var(--accent-blue)" stroke-width="2"/><line x1="10" y1="18" x2="14" y2="18" stroke="var(--accent-blue)" stroke-width="2"/></svg>
      </p>
      <div class="address">PO Box 862<br>Carrowbrook Qld 4179</div>
    </div>
  </article>
</body>
</html>
```